wedding photography website for top wedding photographer

I have a website right now that is barely working. I want the photos to maybe all the photos lined up horizontally and you scroll to see the images. I have an orange logo and want it to be dark grey. I also need a page for publications (I have those as scans) and a link to an About page.

Target Market(s)

wedding planners and bride

Industry/Entity Type

Wedding Photography

Coding

Coded - Design and coding required

Number of Pages Required

5+ page

Font styles to use
Serif
Sans Serif

Colors
ffffff
474747

Requirements
Must have
• easy to navigate, always want the instagram and contact info readily available, should be clean and modern and let the photos stand out. it's wedding photos but i don't want it to feel girly or prissy.
Nice to have
• possibly could be one big photo on the home page, then click it to go into all the other photos. want page options on the home page and every page
Should not have
• nothing fussy or quaint, want this to be the "Copper Ladle" restaurant of wedding photography

```html
<!DOCTYPE html>
<html lang="en">
<head>
<meta charset="utf-8">
<title>Ivory Lane Photography</title>
<link href="https://fonts.googleapis.com/css2?family=Raleway:wght@300;400;600&family=Open+Sans:wght@400;600&display=swap" rel="stylesheet">
<style>
  :root{
    --accent:#474747;
    --accent-soft:#d6d6d6;
    --ink:#474747;
    --muted:#8a8a8a;
    --line:#e4e4e4;
    --paper:#ffffff;
    --haze:#f4f4f4;
    --dark:#2b2b2b;
    --footer:#efefef;
  }
  *{box-sizing:border-box;margin:0;padding:0}
  html,body{width:711px;height:1200px;overflow:hidden}
  body{background:var(--paper);font-family:"Open Sans",Arial,sans-serif;color:var(--ink);position:relative}
  .backdrop{position:absolute;left:0;top:0;width:711px;height:430px;
    background:radial-gradient(ellipse at 90% 20%,#d8d8d8 0%,transparent 45%),radial-gradient(ellipse at 8% 25%,#e0e0e0 0%,transparent 45%),linear-gradient(#eeeeee,#fafafa 90%,#fff)}
  .page{position:absolute;left:135px;width:441px;top:0}
  .site-header{height:47px;display:flex;align-items:center;justify-content:space-between;background:var(--paper);padding:0 6px}
  .brand{font-family:"Raleway",sans-serif;font-weight:400;font-size:12px;color:var(--ink)}
  .nav-wrap{display:flex;flex-direction:column;align-items:flex-end;gap:4px}
  .social{display:flex;gap:4px}
  .social span{width:5px;height:5px;border-radius:50%;background:var(--muted)}
  .nav{display:flex;gap:2px;list-style:none}
  .nav li{font-family:"Raleway",sans-serif;font-size:6px;padding:4px 5px;color:var(--ink)}
  .nav li.active{background:var(--accent);color:#fff}
  .hero{height:166px;background:linear-gradient(90deg,#3a3a3a,#7d7b7c 35%,#bdb9bb 55%,#6f6d6e 80%,#434343);position:relative}
  .hero-caption{position:absolute;right:60px;bottom:22px;font-family:"Raleway",sans-serif;font-size:7px;color:#fff}
  .about{height:202px;text-align:center;padding-top:30px;background:var(--paper)}
  .section-title{font-family:"Raleway",sans-serif;font-weight:300;color:var(--accent);font-size:20px}
  .about p{font-size:5.5px;line-height:9px;color:var(--muted);width:260px;margin:10px auto 0}
  .btn{display:inline-block;background:var(--accent);color:#fff;font-family:"Raleway",sans-serif;font-size:6.5px;padding:4px 12px;border-radius:2px}
  .about .btn{margin-top:14px}
  .ribbon{margin:14px auto 0;width:280px;height:24px;background:var(--haze);border:1px solid var(--line);font-size:5px;color:var(--muted);display:flex;align-items:center;justify-content:center}
  .feature{position:absolute;left:135px;width:441px;height:142px;display:flex;align-items:center;gap:16px}
  .feature .photo{width:204px;height:132px;border:4px solid #fff;box-shadow:0 0 3px rgba(0,0,0,.25)}
  .feature .copy{flex:1}
  .feature h3{font-family:"Raleway",sans-serif;font-weight:400;font-size:9px;color:var(--ink);margin-bottom:6px}
  .feature p{font-size:5.5px;line-height:9px;color:var(--muted);margin-bottom:8px}
  .feature-one{top:427px}
  .feature-one .photo{background:linear-gradient(135deg,#5d7fa8,#b6d0ea 45%,#3d4a66)}
  .feature-two{top:604px}
  .feature-two .copy{padding-left:6px}
  .feature-two .photo{background:linear-gradient(#6fb3d9,#a9d6ec 45%,#e5d9c1 70%,#c7b79a)}
  .gallery{position:absolute;top:758px;left:0;width:711px;height:154px;display:flex}
  .gallery div{flex:1}
  .g1{background:linear-gradient(135deg,#2d3a4a,#c7b6ad,#3b3f4a)}
  .g2{background:linear-gradient(#c9c58c,#6f8d4a 60%,#3f4a2b)}
  .g3{background:var(--accent-soft);display:flex;align-items:center;justify-content:center;font-family:"Raleway",sans-serif;font-size:9px;color:#fff}
  .g4{background:linear-gradient(#8fd0d8,#3fb1b8 50%,#e8e1d6)}
  .g5{background:linear-gradient(135deg,#f1ede6,#d8cdbd,#f4efe8)}
  .newsletter{position:absolute;top:912px;left:0;width:711px;height:202px;background:linear-gradient(90deg,#2c2620,#6b5a3e 30%,#8a7650 50%,#3a3128)}
  .signup{position:absolute;left:303px;top:28px;width:266px;height:132px;background:rgba(30,30,30,.85);padding:14px 20px;color:#fff}
  .signup h2{font-family:"Raleway",sans-serif;font-weight:300;font-size:17px}
  .signup p{font-size:5.5px;line-height:8px;color:#ccc;margin:6px 0 8px}
  .field{width:160px;height:13px;background:#fff;font-size:5.5px;color:#999;padding:3px 5px;margin-bottom:8px}
  .signup .btn{background:#fff;color:var(--dark)}
  .footer{position:absolute;top:1114px;left:0;width:711px;height:86px;background:var(--footer);text-align:center;padding-top:22px}
  .footer p{font-size:5.5px;line-height:9px;color:var(--muted);width:340px;margin:0 auto}
  .footer .legal{margin-top:10px}
</style>
</head>
<body>
<div class="backdrop" role="img" aria-label="Soft blurred wedding photograph in the background"></div>
<div class="page">
  <header class="site-header">
    <div class="brand">Ivory Lane Photography</div>
    <div class="nav-wrap">
      <div class="social"><span></span><span></span><span></span><span></span></div>
      <ul class="nav">
        <li class="active">Home</li><li>About</li><li>Portfolio</li><li>Publications</li><li>Blog</li><li>Contact</li>
      </ul>
    </div>
  </header>
  <div class="hero" role="img" aria-label="Collage of wedding couples dancing and posing">
    <span class="hero-caption">Ivory Lane Photography</span>
  </div>
  <section class="about">
    <h1 class="section-title">About Us</h1>
    <p>We capture honest, unhurried moments on your wedding day, with a calm eye for light and detail. Every story is told in clean, timeless frames that let the people and the place speak for themselves.</p>
    <p>From the first look to the last dance, we stay close but quiet, so nothing feels staged.</p>
    <span class="btn">Read More</span>
    <div class="ribbon">Booking now for the coming season — limited dates remain.</div>
  </section>
</div>

<section class="feature feature-one">
  <div class="photo" role="img" aria-label="Bride and groom walking under sparkling lights"></div>
  <div class="copy">
    <h3>Wedding photography</h3>
    <p>Natural light, relaxed direction and a documentary approach shape every gallery we deliver to our couples.</p>
    <span class="btn">View Profile</span>
  </div>
</section>

<section class="feature feature-two">
  <div class="copy">
    <h3>Wedding photography</h3>
    <p>Each collection is edited by hand, printed on archival paper and delivered in a simple linen box.</p>
    <span class="btn">View Profile</span>
  </div>
  <div class="photo" role="img" aria-label="Couple embracing on rocks by the sea"></div>
</section>

<section class="gallery">
  <div class="g1" role="img" aria-label="Bride and groom portrait with bouquet"></div>
  <div class="g2" role="img" aria-label="Couple in a sunlit field"></div>
  <div class="g3">A wedding photo</div>
  <div class="g4" role="img" aria-label="Beach ceremony with turquoise drapes"></div>
  <div class="g5" role="img" aria-label="Decorated reception tables"></div>
</section>

<section class="newsletter" role="img" aria-label="Couple in a golden field at sunset">
  <div class="signup">
    <h2>Join Our Newsletter</h2>
    <p>Sign up for seasonal offers, new galleries and planning notes for your day.</p>
    <div class="field">Your email address</div>
    <span class="btn">Subscribe</span>
  </div>
</section>

<footer class="footer">
  <p>Ivory Lane Photography · Natural wedding photography for couples and planners. Available for travel worldwide.</p>
  <p class="legal">Copyright © 2024 Ivory Lane Photography. All rights reserved.</p>
</footer>
</body>
</html>
```